CEO Invite for Breakfast Event - Paper Printing

Using our logo that appears on our website coralbridgecollective.org and attached - we need a very quick turn around for paper invite design that we can send out to the top CEOs in Australia in less than 24 hours.

The invite is for a CEO breakfast. It will be printed on paper.

The design chosen will have the best of these qualities without saying them outright (subtle!):

Corporate
VIP
CEO
Equality
Human Rights
Standing Up
Supporting

There will be text on the invite explaining what the invite is for and who is invited as well as RSVP etc.

Target Market(s)

CEOs of Australia

Industry/Entity Type

Printing

Requirements
Must have
• A space to write the invite information

```html
<!DOCTYPE html>
<html lang="en">
<head>
<meta charset="utf-8">
<title>Coral Bridge Collective – CEO Breakfast Invitation</title>
<link rel="stylesheet" href="https://fonts.googleapis.com/css2?family=Cinzel:wght@400;600&family=Roboto+Condensed:wght@700&display=swap">
<style>
  :root {
    --page: #eeeae4;
    --brand-blue: #4a88c9;
    --brand-blue-dark: #3a72b0;
    --sky: #5ba7cc;
    --sky-light: #cfe3ea;
    --silhouette: #1a2236;
    --panel: #222326;
    --panel-dark: #121314;
    --ink-light: #ffffff;
  }
  * { box-sizing: border-box; margin: 0; padding: 0; }
  html, body {
    width: 1200px; height: 729px; overflow: hidden;
    background: var(--page);
  }
  .invite {
    position: absolute;
    left: 40px; top: 88px;
    width: 820px; height: 405px;
    transform: scale(1.3659);
    transform-origin: 0 0;
    overflow: hidden;
    box-shadow: 0 2px 6px rgba(0,0,0,.25);
  }
  .invite__photo {
    position: absolute; inset: 0 0 35px 0;
    background:
      radial-gradient(ellipse 120px 70px at 720px 180px, rgba(235,240,236,.85), transparent 70%),
      radial-gradient(ellipse 90px 50px at 560px 250px, rgba(240,236,220,.9), transparent 70%),
      radial-gradient(ellipse 150px 110px at 330px 170px, rgba(20,28,48,.95), transparent 75%),
      linear-gradient(90deg, var(--silhouette) 0%, #2c3a58 30%, var(--sky) 65%, #3d93bf 100%);
  }
  .invite__band {
    position: absolute; left: 0; right: 0; bottom: 0; height: 35px;
    background: var(--brand-blue);
  }
  .brand-tab {
    position: absolute; left: 38px; top: 0;
    width: 90px; height: 170px;
    background: var(--brand-blue);
    display: flex; flex-direction: column; justify-content: flex-end;
    padding: 0 6px 22px;
  }
  .brand-tab__name {
    font-family: "Roboto Condensed", sans-serif;
    font-weight: 700; font-size: 13px; line-height: 1.05;
    color: var(--ink-light); text-transform: uppercase;
    text-align: center;
  }
  .message {
    position: absolute; left: 160px; right: 100px; top: 150px;
    text-align: center; color: var(--ink-light);
    font-family: "Cinzel", serif;
    text-shadow: 0 1px 3px rgba(0,0,0,.6);
  }
  .message__title { font-size: 26px; font-weight: 400; letter-spacing: 1px; line-height: 1; margin-bottom: 6px; }
  .message__hosts { font-size: 11.5px; line-height: 19px; }
  .message__purpose { font-size: 13px; line-height: 18px; margin-top: 1px; }
  .details { position: absolute; inset: 0; }
  .detail {
    position: absolute;
    background: linear-gradient(180deg, var(--panel), var(--panel-dark));
    box-shadow: 0 3px 8px rgba(0,0,0,.55);
  }
  .detail__label {
    display: block; height: 22px;
    background: linear-gradient(180deg, var(--brand-blue), var(--brand-blue-dark));
    color: var(--ink-light);
    font-family: "Roboto Condensed", sans-serif; font-weight: 700;
    font-size: 14px; line-height: 24px; text-align: center;
  }
  .detail--where { left: 188px; top: 280px; width: 145px; height: 72px; }
  .detail--date  { left: 493px; top: 272px; width: 145px; height: 73px; }
  .detail--rsvp  { left: 333px; top: 268px; width: 160px; height: 94px; z-index: 1; }
  .detail--rsvp .detail__label { height: 32px; font-size: 19px; line-height: 32px; }
</style>
</head>
<body>
  <article class="invite">
    <div class="invite__photo" role="img" aria-label="Photo of two hands forming a heart shape silhouetted against a bright blue sky with clouds and golden grass"></div>
    <div class="invite__band"></div>

    <div class="brand-tab">
      <p class="brand-tab__name">Coral<br>Bridge<br>Collective<br>.org</p>
    </div>

    <section class="message">
      <h1 class="message__title">Invitation</h1>
      <p class="message__hosts">Coral Bridge Collective, the Harbourline Inclusion Council<br>and Marlow + Finch invite you to</p>
      <p class="message__purpose">a breakfast with and to discuss corporate<br>support for marriage equality</p>
    </section>

    <div class="details">
      <div class="detail detail--where"><span class="detail__label">WHERE</span></div>
      <div class="detail detail--rsvp"><span class="detail__label">RSVP</span></div>
      <div class="detail detail--date"><span class="detail__label">DATE</span></div>
    </div>
  </article>
</body>
</html>
```